Tarek & Lubna's 50th Anniversary Celebration & Reunion

I need a flyer to send out via email and for posting on facebook to invite guests to a 50th wedding anniversary / family reunion.

Location is sunny La Jolla CA the Jewel of San Diego's Coast.

Week long daily activities starting Mon July 28-Aug 1st Friday, The event will be on Wednesday.
* Daily Catered Family Breakfast at the Marlow Hall of La Jolla
* Daily group activities including
*Exploring La Jolla Beaches & Ocean Cave Kayaking
*TideLand Private Behind the Scenes Tour
*World Famous Harbor Wild Park
*Sunset Balloon Ride
*Private Yatch on the Bay

Actual Anniversary event will take place Thursday December 28, 2013 at 5pm at the Marlow Hall.

There are many local hotels around the Marlow Hall. 4512 Pell Ave, La Jolla, CA 92037

Host is Remond and the entire Halabi Family. For questions, please email Remond@thegrovefeasts.com

Target Market(s)

all ages from 10 year olds to 70 year olds. Should appeal to all

Industry/Entity Type

Wedding

Font styles to use
Script

Colors

Designer to choose colors to be used in the design.

Requirements
Must have
• Fun graphics, including one with a stretch limo as there will be one available

Nice to have
• Logo for TideLand Inserting a picture of an actual wedding 50 years ago or so of the bride and groom. incorporating the limo cropped out of the picture attached would also be nice

```html
<!DOCTYPE html>
<html lang="en">
<head>
<meta charset="utf-8">
<title>Join us in La Jolla – 50th Anniversary Celebration</title>
<link rel="stylesheet" href="https://fonts.googleapis.com/css2?family=Bowlby+One+SC&family=Didact+Gothic&family=Rouge+Script&display=swap">
<style>
  :root {
    --orange: #f27a35;
    --turquoise: #45c2cc;
    --cream: #f8f0c6;
    --ink: #141414;
    --navy: #123e73;
    --photo-light: #cfcfcf;
    --photo-dark: #3a3a3a;
  }
  html, body { margin: 0; padding: 0; overflow: hidden; background: #ffffff; }
  .flyer {
    position: relative;
    width: 927px;
    height: 1200px;
    overflow: hidden;
    background: var(--turquoise);
    color: var(--ink);
    font-family: "Didact Gothic", "Century Gothic", sans-serif;
  }
  .backdrop { position: absolute; inset: 0; }
  .flyer p, .flyer h1, .flyer h2, .flyer ul { margin: 0; padding: 0; }
  .abs { position: absolute; }

  .headline {
    left: 44px; top: 14px;
    font-family: "Bowlby One SC", Impact, sans-serif;
    font-weight: 400;
    font-size: 60px;
    line-height: 1;
    color: var(--cream);
    white-space: nowrap;
  }
  .headline .place { font-size: 80px; }
  .tagline {
    left: 440px; top: 92px;
    font-family: "Rouge Script", cursive;
    font-size: 46px;
    line-height: 1;
    color: var(--ink);
    transform: rotate(-4deg);
    white-space: nowrap;
  }
  .hosts {
    left: 436px; top: 176px;
    font-size: 44px; line-height: 50px;
    text-align: center;
    width: 480px;
  }
  .contact { left: 366px; top: 318px; width: 540px; text-align: center; }
  .contact .ask { font-size: 44px; line-height: 50px; }
  .contact .email { font-size: 32px; line-height: 40px; }
  .hotels {
    right: 26px; top: 482px;
    font-size: 20px; line-height: 24px;
    text-align: right;
  }

  .section-title {
    font-family: "Bowlby One SC", Impact, sans-serif;
    font-weight: 400;
    color: var(--ink);
    white-space: nowrap;
  }
  .celebration { left: 15px; top: 352px; }
  .celebration .section-title { font-size: 30px; line-height: 40px; }
  .event-details {
    margin-top: 18px !important;
    font-size: 25px; line-height: 38px;
    font-variant: small-caps;
  }

  .activities { left: 15px; top: 630px; }
  .activities .section-title { font-size: 26px; line-height: 34px; }
  .activity-list { list-style: none; margin-top: 18px !important; }
  .activity-list li { font-size: 29px; line-height: 27px; margin-bottom: 27px; white-space: nowrap; }

  .portrait {
    left: 458px; top: 750px;
    width: 410px; height: 410px;
    border-radius: 50%;
    background: radial-gradient(circle at 50% 40%, var(--photo-light), #8d8d8d 60%, var(--photo-dark));
  }

  .partner {
    left: 15px; top: 1112px;
    display: flex; align-items: center; gap: 8px;
    font-size: 28px; line-height: 32px; color: var(--navy);
  }
  .partner .dot { width: 16px; height: 16px; border-radius: 50%; background: var(--navy); }

  .closing {
    left: 15px; top: 1160px;
    font-family: "Rouge Script", cursive;
    font-size: 27px; line-height: 30px; color: var(--ink);
    white-space: nowrap;
  }
</style>
</head>
<body>
<main class="flyer">
  <svg class="backdrop" viewBox="0 0 927 1200" width="927" height="1200" aria-hidden="true">
    <path fill="var(--orange)" d="M0 0 H927 V700 H700 C560 560 420 440 250 330 C160 270 80 210 0 170 Z"/>
    <circle cx="663" cy="955" r="250" fill="var(--orange)"/>
    <path fill="var(--orange)" d="M600 1180 C730 1160 850 1100 927 1040 V1080 C840 1140 720 1195 600 1180 Z"/>
  </svg>

  <h1 class="abs headline">Join us in <span class="place">La Jolla!</span></h1>
  <p class="abs tagline">the jewel of San Diegos coast</p>

  <p class="abs hosts">Hosted by Remond and<br>the Halabi Family</p>

  <div class="abs contact">
    <p class="ask">For questions please email</p>
    <p class="email">remond@thegrovefeasts.com</p>
  </div>

  <p class="abs hotels">There are several local hotels<br>located near the Marlow Hall<br>for your convenience.</p>

  <section class="abs celebration">
    <h2 class="section-title">50th Anniversary<br>Celebration</h2>
    <p class="event-details">Thursday December 28, 2013<br>5:00 PM<br>Marlow Hall of La Jolla<br>4512 Pell Ave., La Jolla, CA 92037</p>
  </section>

  <section class="abs activities">
    <h2 class="section-title">Week Long Family Reunion Activities</h2>
    <ul class="activity-list">
      <li>Daily catered family breakfast at the<br>Marlow Hall of La Jolla</li>
      <li>Exploring La Jolla Beaches and<br>Ocean Cave Kayaking</li>
      <li>TideLand Private Behind the<br>Scenes Tour</li>
      <li>World Famous Harbor Wild Park</li>
      <li>Sunset Balloon Ride</li>
      <li>Private Yacht on the Bay</li>
    </ul>
  </section>

  <div class="abs portrait" role="img" aria-label="Black and white wedding photograph of the bride and groom from fifty years ago"></div>

  <div class="abs partner"><span class="dot"></span><span>TideLand</span></div>

  <p class="abs closing">activities will begin on December 26 and commence on New Years Eve</p>
</main>
</body>
</html>
```